Computer screen desktop background design for dentists orthodontic office PCs

We need a new design to use as the Windows desktop background picture for the PC workstations in a dentists orthodontic office.
The design should be vector graphics.
The aspect ratio should reflect the monitor size (Resolution: 1920x1200).
In the uploaded files you can find the logo, the fonts and the design of the business card.
The design should not be brighter than the Windows 10 background picture (monitor lifetime).

The office logo must be the dominating part of the design (see uploaded files).

You don't need to use the same fonts, but the used fonts have to be in harmony with the fonts used in the logo and the business card.
The colors used have to be in harmony with the logo.
All the text below must be on the design.
The logical text groups are separated by empty lines.

Kieferorthopädie Brunnweid

Dr. med. dent. Anton Vrabec
Fachzahnarzt für Kieferorthopädie (CH) (Important information!)

Please make something cool and modern that attracts the patient's attraction when seen on the monitor screen.

Target Market(s)

dentists orthodontic office

Industry/Entity Type

Computer

Font styles to use
Sans Serif

Colors

Designer to choose colors to be used in the design.

Requirements
Must have
• The design should be vector graphics.
• The aspect ratio should reflect the monitor size (Resolution: 1920x1200).
• In the uploaded files you can find the logo, the fonts and the design of the business card.
• The design should not be brighter than the Windows 10 background picture (monitor lifetime).
• The office logo must be the dominating part of the design (see uploaded files).
• You don't need to use the same fonts, but the used fonts have to be in harmony with the fonts used in the logo and the business card.
• The colors used have to be in harmony with the logo.
• All the text below must be on the design.
• The logical text groups are separated by empty lines.
• Kieferorthopädie Brunnweid
• Dr. med. dent. Anton Vrabec
• Fachzahnarzt für Kieferorthopädie (CH) (Important information!)
• Adobe Illustrator source files
Nice to have
• Please make something cool and modern that attracts the patient's attraction when seen on the monitor screen.
Should not have

```html
<!DOCTYPE html>
<html lang="de">
<head>
<meta charset="utf-8">
<title>Kieferorthopädie Brunnweid – Desktop</title>
<link rel="stylesheet" href="https://fonts.googleapis.com/css2?family=Roboto:wght@400;700&family=Roboto+Condensed:wght@500&display=swap">
<style>
  :root {
    --navy-deep: #081a66;
    --navy: #0b2a8c;
    --blue-mid: #1446b4;
    --blue-light: #27b2ee;
    --disc-light: #f5f8fa;
    --disc-shade: #dde5ec;
    --logo-navy: #0c1f63;
    --text: #ffffff;
  }
  * { margin: 0; padding: 0; box-sizing: border-box; }
  html, body {
    width: 1200px;
    height: 732px;
    overflow: hidden;
    background: var(--navy-deep);
  }
  .wallpaper {
    position: relative;
    width: 1200px;
    height: 732px;
    overflow: hidden;
    background: linear-gradient(160deg, var(--navy-deep) 0%, var(--navy) 55%, var(--blue-mid) 100%);
  }
  .wave-field {
    position: absolute;
    inset: 0;
    background:
      radial-gradient(ellipse 620px 260px at 960px 700px, rgba(39, 178, 238, 0.45), rgba(39, 178, 238, 0) 70%),
      radial-gradient(ellipse 520px 160px at 900px 90px, rgba(39, 150, 238, 0.22), rgba(39, 150, 238, 0) 70%);
  }
  .logo-disc {
    position: absolute;
    left: -140px;
    top: 30px;
    width: 740px;
    height: 740px;
    border-radius: 50%;
    background: radial-gradient(circle at 45% 40%, var(--disc-light) 0%, var(--disc-light) 45%, var(--disc-shade) 100%);
  }
  .practice-mark {
    position: absolute;
    left: 60px;
    top: 365px;
    width: 400px;
    display: flex;
    align-items: center;
    justify-content: center;
    gap: 16px;
  }
  .practice-mark__dot {
    width: 34px;
    height: 34px;
    border-radius: 50%;
    background: var(--blue-light);
    flex: none;
  }
  .practice-mark__name {
    font-family: "Roboto", sans-serif;
    font-weight: 700;
    font-size: 52px;
    color: var(--logo-navy);
    line-height: 1;
  }
  .identity {
    position: absolute;
    left: 634px;
    top: 262px;
    color: var(--text);
  }
  .identity__practice {
    font-family: "Roboto", sans-serif;
    font-weight: 700;
    font-size: 60px;
    line-height: 66px;
    letter-spacing: -0.5px;
  }
  .identity__doctor {
    margin-top: 34px;
    font-family: "Roboto Condensed", sans-serif;
    font-weight: 500;
    font-size: 34px;
    line-height: 40px;
  }
  .identity__title {
    margin-top: 8px;
    font-family: "Roboto", sans-serif;
    font-weight: 400;
    font-size: 17px;
    letter-spacing: 2px;
    line-height: 24px;
  }
</style>
</head>
<body>
  <main class="wallpaper">
    <div class="wave-field" role="img" aria-label="Fliessende hellblaue Linienwellen auf dunkelblauem Grund"></div>
    <div class="logo-disc"></div>
    <div class="practice-mark">
      <span class="practice-mark__dot"></span>
      <span class="practice-mark__name">Brunnweid</span>
    </div>
    <section class="identity">
      <h1 class="identity__practice">Kieferorthopädie<br>Brunnweid</h1>
      <p class="identity__doctor">Dr. med. dent. Anton Vrabec</p>
      <p class="identity__title">Fachzahnarzt für Kieferorthopädie (CH)</p>
    </section>
  </main>
</body>
</html>
```